Physiotherapiepraxis braucht Druckvorlage für Werbeanzeige
Zielgruppe
Dienstleistung im Gesundheitswesen als Physiotherapiepraxis.
Krankengymnastik, auch im häuslichen Bereich oder im Altersheim, und Massage sowie Wellnessanwendungen.
Zielgruppe sind primär Erwachsene, eingeschränkt auch Kinder.
Aufgabenstellung
Ich möchte eine Druckvorlage für eine Werbeanzeige, die ich immer mal wieder in verschiedenen Festschriften im dörflichen Bereich oder in einer regionalen Zeitschrift veröffentlichen kann.
Die Anzeige soll das Logo enthalten und die Anschrift der Praxis sowie die Telefonnummer und Adresse der Homepage.

```html
<!DOCTYPE html>
<html lang="de">
<head>
<meta charset="utf-8">
<title>Anzeige Physiotherapie Marlene Kötter</title>
<link rel="stylesheet" href="https://fonts.googleapis.com/css2?family=Open+Sans:wght@400;600;700&family=Caveat:wght@400&display=swap">
<style>
  :root {
    --practice-green: #1d7a3a;
    --practice-gold: #d3b52b;
    --paper: #ffffff;
    --frame: #3a3a3a;
    --backdrop: #eeeeea;
  }
  * { box-sizing: border-box; margin: 0; padding: 0; }
  html, body {
    width: 1200px;
    height: 775px;
    overflow: hidden;
    background: var(--backdrop);
    font-family: "Open Sans", Arial, sans-serif;
  }
  .advert {
    position: absolute;
    left: 270px;
    top: 37px;
    width: 660px;
    height: 700px;
    background: var(--paper);
    border: 3px solid var(--frame);
    padding: 0 40px;
  }
  .practice-name {
    display: flex;
    align-items: center;
    justify-content: center;
    gap: 18px;
    height: 186px;
    padding-top: 40px;
    color: var(--practice-green);
    font-size: 44px;
    font-weight: 400;
    letter-spacing: 5px;
  }
  .name-dot {
    width: 26px;
    height: 26px;
    border-radius: 50%;
    background: var(--practice-gold);
    flex: none;
  }
  .service-band {
    height: 89px;
    background: var(--practice-gold);
    color: var(--paper);
    font-weight: 700;
    font-size: 50px;
    letter-spacing: 1px;
    display: flex;
    align-items: center;
    justify-content: center;
  }
  .info-box {
    margin-top: 23px;
    height: 358px;
    border: 3px solid var(--practice-green);
    padding: 20px 18px 0 18px;
    color: var(--practice-green);
    overflow: hidden;
  }
  .slogan {
    font-family: "Caveat", cursive;
    font-size: 64px;
    line-height: 64px;
    margin-bottom: 24px;
  }
  .slogan span { display: block; }
  .slogan .second-line { padding-left: 88px; }
  .contact-list { list-style: none; }
  .contact-list li {
    display: flex;
    align-items: center;
    gap: 8px;
    font-size: 30px;
    line-height: 52px;
    letter-spacing: -0.3px;
    white-space: nowrap;
  }
  .contact-icon {
    width: 24px;
    height: 24px;
    flex: none;
    fill: var(--practice-green);
  }
</style>
</head>
<body>
  <main class="advert">
    <header class="practice-name">
      <span>Marlene Kötter</span>
      <span class="name-dot"></span>
    </header>
    <div class="service-band">PHYSIOTHERAPIE</div>
    <section class="info-box">
      <p class="slogan">
        <span>Wir bringen Sie</span>
        <span class="second-line">gerne in Bewegung</span>
      </p>
      <ul class="contact-list">
        <li>
          <svg class="contact-icon" viewBox="0 0 24 24" aria-hidden="true">
            <path d="M12 1.5c-4.1 0-7.2 3.1-7.2 7.1 0 5.3 7.2 13.9 7.2 13.9s7.2-8.6 7.2-13.9c0-4-3.1-7.1-7.2-7.1zm0 10a3 3 0 1 1 0-6 3 3 0 0 1 0 6z"/>
          </svg>
          Lindenweg 7 in 24598 Hollmark
        </li>
        <li>
          <svg class="contact-icon" viewBox="0 0 24 24" aria-hidden="true">
            <path d="M6.6 10.8c1.4 2.8 3.8 5.1 6.6 6.6l2.2-2.2c.3-.3.7-.4 1-.2 1.1.4 2.3.6 3.6.6.6 0 1 .4 1 1V20c0 .6-.4 1-1 1C10.6 21 3 13.4 3 4c0-.6.4-1 1-1h3.5c.6 0 1 .4 1 1 0 1.3.2 2.5.6 3.6.1.3 0 .7-.2 1L6.6 10.8z"/>
          </svg>
          +49 (0) 4321 - 47 20 65
        </li>
        <li>
          <svg class="contact-icon" viewBox="0 0 24 24" aria-hidden="true">
            <circle cx="12" cy="12" r="10" fill="none" stroke="#1d7a3a" stroke-width="2"/>
            <ellipse cx="12" cy="12" rx="4.5" ry="10" fill="none" stroke="#1d7a3a" stroke-width="2"/>
            <path d="M2 12h20" stroke="#1d7a3a" stroke-width="2"/>
          </svg>
          www.physiotherapie-hollmark.de
        </li>
      </ul>
    </section>
  </main>
</body>
</html>
```